Moder Business Card Design for Renewables Business

Need a business card design for my business. We collect & repurpose spent coffee ground from cafes. The cards will be made from recycled paper. Needs to fit our corporate colour scheme of white, green & brown (see logo for colour codes). Eco friendly, modern, intresting & eye catching.
This card needs to convey the message of the business and fit into its mantra of eco-friendly, sustainable etc.

Target Market(s)

Cafe Owners, Coffee Drinkers, Recycling Companies, Farmers

Industry/Entity Type

Recycling

Contact Information for Business Card

Name; Peter Halloran
Phone; 0412 386 527
e-mail; info@lumatrove.com.au
website; www.lumatrove.com.au

Font styles to use
Sans Serif
Script

Colors

Designer to choose colors to be used in the design.

Requirements
Must have
• FRONT;
• Logo, Name (Peter Halloran), phone number, e-mail address, website
• BACK;
• On the back in cursive text; 'GROUNDS FOR A GREENER TOMORROW'
• Small facebook & Instagram logos with text 'Lumatrove'
Should not have
• messy design

```html
<!DOCTYPE html>
<html lang="en">
<head>
<meta charset="utf-8">
<title>Lumatrove Business Card</title>
<link href="https://fonts.googleapis.com/css2?family=Open+Sans:wght@400;600;700&display=swap" rel="stylesheet">
<style>
  :root {
    --stage: #3a3a3a;
    --stage-light: #5a5a5a;
    --kraft: #cbb68e;
    --kraft-light: #d6c39d;
    --kraft-dark: #bda67b;
    --brown: #5a3318;
    --green: #5f9a45;
    --ink: #1f1a14;
  }
  * { margin: 0; padding: 0; box-sizing: border-box; }
  html, body { width: 1200px; height: 1028px; overflow: hidden; }
  body {
    background: radial-gradient(ellipse at 55% 40%, var(--stage-light), var(--stage) 75%);
    font-family: "Open Sans", Arial, sans-serif;
    position: relative;
  }
  .card {
    position: absolute;
    width: 760px;
    height: 464px;
    background: linear-gradient(135deg, var(--kraft-light), var(--kraft) 50%, var(--kraft-dark));
    border-radius: 4px;
    box-shadow: 0 18px 40px rgba(0,0,0,0.45);
    overflow: hidden;
  }
  .card-back { left: 390px; top: 44px; }
  .card-front { left: 50px; top: 530px; }

  /* back */
  .tagline {
    position: absolute; top: 46px; left: 0; right: 0;
    text-align: center; font-weight: 700; font-size: 27px;
    letter-spacing: 0.5px; color: var(--ink);
  }
  .brand-lockup {
    position: absolute; left: 0; right: 0; top: 130px;
    display: flex; flex-direction: column; align-items: center; gap: 16px;
  }
  .brand-dot {
    width: 110px; height: 110px; border-radius: 50%;
    background: var(--green);
  }
  .brand-name {
    font-weight: 600; font-size: 40px; letter-spacing: 1px;
    color: var(--brown); text-transform: uppercase;
  }
  .social-links {
    position: absolute; left: 0; right: 0; bottom: 48px;
    text-align: center; font-size: 19px; color: var(--ink);
  }
  .social-links .sep { margin: 0 12px; }

  /* front */
  .front-brand {
    position: absolute; left: 60px; top: 130px; width: 240px;
    display: flex; flex-direction: column; align-items: center; gap: 14px;
  }
  .front-brand .brand-dot { width: 120px; height: 120px; }
  .front-brand .brand-name { font-size: 28px; }
  .divider {
    position: absolute; left: 340px; top: 70px; width: 3px; height: 320px;
    background: var(--brown);
  }
  .contact-block { position: absolute; left: 385px; top: 120px; }
  .person-name {
    font-weight: 600; font-size: 36px; letter-spacing: 1px;
    text-transform: uppercase; color: var(--ink);
  }
  .person-name .first { color: var(--green); }
  .name-rule { width: 330px; height: 3px; background: var(--brown); margin: 6px 0 22px; }
  .contact-list { list-style: none; }
  .contact-list li {
    display: flex; align-items: center; gap: 14px;
    font-size: 23px; color: var(--ink); margin-bottom: 14px;
  }
  .contact-list svg { width: 24px; height: 24px; flex: none; }
</style>
</head>
<body>

<section class="card card-back" aria-label="Card back">
  <p class="tagline">GROUNDS FOR A GREENER TOMORROW</p>
  <div class="brand-lockup">
    <span class="brand-dot"></span>
    <span class="brand-name">Lumatrove</span>
  </div>
  <p class="social-links">facelink.com/lumatrove<span class="sep">/</span>snapgram.com/lumatrove</p>
</section>

<section class="card card-front" aria-label="Card front">
  <div class="front-brand">
    <span class="brand-dot"></span>
    <span class="brand-name">Lumatrove</span>
  </div>
  <div class="divider"></div>
  <div class="contact-block">
    <h1 class="person-name"><span class="first">Peter</span> Halloran</h1>
    <div class="name-rule"></div>
    <ul class="contact-list">
      <li>
        <svg viewBox="0 0 24 24" aria-hidden="true"><path fill="#5a3318" d="M6.6 10.8c1.4 2.8 3.8 5.1 6.6 6.6l2.2-2.2c.3-.3.7-.4 1-.2 1.1.4 2.3.6 3.6.6.6 0 1 .4 1 1V20c0 .6-.4 1-1 1C10.6 21 3 13.4 3 4c0-.6.4-1 1-1h3.5c.6 0 1 .4 1 1 0 1.3.2 2.5.6 3.6.1.3 0 .7-.2 1z"/></svg>
        0412 386 527
      </li>
      <li>
        <svg viewBox="0 0 24 24" aria-hidden="true"><rect x="2" y="5" width="20" height="14" rx="1" fill="#5a3318"/><path d="M3 6l9 7 9-7" fill="none" stroke="#cbb68e" stroke-width="1.6"/></svg>
        info@lumatrove.com.au
      </li>
      <li>
        <svg viewBox="0 0 24 24" aria-hidden="true"><circle cx="12" cy="12" r="10" fill="#5a3318"/><g fill="none" stroke="#cbb68e" stroke-width="1.3"><ellipse cx="12" cy="12" rx="4" ry="10"/><path d="M2 12h20M4 7h16M4 17h16M12 2v20"/></g></svg>
        www.lumatrove.com.au
      </li>
    </ul>
  </div>
</section>

</body>
</html>
```